We Buy Houses Postcard Design

Harborline Estate Traders is one of Baltimore‘s top real estate investing groups because we treat buyers and sellers like real people; not like numbers on a spreadsheet. We specialize in buying distressed properties including multi-family, commercial, retail, single family, and bank REO’s from sellers who need to sell fast. Our website is www.harborlineestatetraders.com. Our phone number is (443) 517-2094. Both need to be on the card. Front and back sides are to be printed. Front full color, back black and white. We want our logo on the design somewhere. The logo can be found on the website. If you need the original files ask me for them. See attached as examples. Return address should be 487 W Quillfern Ave, Suite 316, Baltimore, MD 21202. My name is Marcus. Address label is 1" x 2-5/8". Please leave room for it and postage on the back side.

Industry/Entity Type

Real Estate

```html
<!DOCTYPE html>
<html lang="en">
<head>
<meta charset="utf-8">
<title>We Buy Houses – Harborline Estate Traders</title>
<link href="https://fonts.googleapis.com/css2?family=Arimo:wght@400;700&display=swap" rel="stylesheet">
<style>
  :root {
    --backdrop: #221c27;
    --sign-blue: #0a6aad;
    --panel-navy: #224e77;
    --label-blue: #1d5a8c;
    --white: #ffffff;
    --soft-grey: #dfe6ee;
    --brand-blue: #2a3f9e;
  }
  * { margin: 0; padding: 0; box-sizing: border-box; }
  html, body {
    width: 1200px; height: 1000px; overflow: hidden;
    background: var(--backdrop);
    font-family: "Arimo", Arial, sans-serif;
  }
  .sign {
    position: absolute; left: 101px; top: 141px;
    width: 998px; height: 717px;
    background: var(--sign-blue);
  }
  .headline {
    position: absolute; left: 0; width: 100%;
    text-align: center; color: var(--white);
    font-weight: 700; font-size: 236px; line-height: 1;
    text-shadow: 0 0 14px rgba(255,255,255,0.45);
  }
  .headline--top { top: 56px; transform: scaleX(0.94); }
  .headline--bottom { top: 229px; transform: scaleX(0.81); }
  .benefit {
    position: absolute; top: 471px; height: 63px;
    background: var(--white); color: var(--label-blue);
    font-weight: 700; font-size: 48px;
    display: flex; align-items: center; justify-content: center;
  }
  .benefit--left { left: 0; width: 514px; border-bottom-right-radius: 42px; border-top-right-radius: 8px; }
  .benefit--right { left: 531px; width: 467px; border-top-left-radius: 42px; border-bottom-left-radius: 8px; }
  .contact {
    position: absolute; left: 0; top: 554px;
    width: 641px; height: 137px;
    background: var(--panel-navy); color: var(--white);
    text-align: center;
  }
  .contact__prompt {
    margin-top: 13px; font-size: 26px; font-weight: 700; color: var(--soft-grey);
  }
  .contact__phone {
    margin-top: 4px; font-size: 74px; font-weight: 700; letter-spacing: 1px;
  }
  .brand {
    position: absolute; left: 659px; top: 554px;
    width: 339px; height: 137px;
  }
  .brand__name {
    height: 115px; background: var(--white);
    display: flex; align-items: center; justify-content: center; gap: 12px;
    color: var(--brand-blue); font-size: 26px; font-weight: 700;
    text-align: left; line-height: 1.1; padding: 0 20px;
  }
  .brand__mark { width: 20px; height: 20px; border-radius: 50%; background: var(--brand-blue); flex: none; }
  .brand__url {
    height: 22px; background: var(--panel-navy); color: var(--white);
    font-size: 14px; text-align: center; line-height: 22px;
  }
</style>
</head>
<body>
  <main class="sign">
    <div class="headline headline--top">WE BUY</div>
    <div class="headline headline--bottom">HOUSES</div>
    <div class="benefit benefit--left">ANY CONDITION</div>
    <div class="benefit benefit--right">FAST CLOSING</div>
    <section class="contact">
      <p class="contact__prompt">Contact Us ›</p>
      <p class="contact__phone">443-517-2094</p>
    </section>
    <section class="brand">
      <div class="brand__name"><span class="brand__mark"></span><span>Harborline Estate<br>Traders</span></div>
      <div class="brand__url">www.harborlineestatetraders.com</div>
    </section>
  </main>
</body>
</html>
```